" Empresa em abertura de firma (status), voltada para o segmento de Headhunter / Jobhunter, Coaching e demais serviços administrativos/treinamento relacionados. "

```html
<!DOCTYPE html>
<html lang="pt-BR">
<head>
<meta charset="utf-8">
<title>TalentaPro – Cartão</title>
<link href="https://fonts.googleapis.com/css2?family=Ubuntu:wght@400;500;700&display=swap" rel="stylesheet">
<style>
  :root {
    --bg: #e9e4de;
    --card: #ffffff;
    --brand-blue: #1f4f9a;
    --curve-blue: #2a5fb8;
    --name-green: #7cb342;
    --text-dark: #1a2a5a;
    --text-grey: #4a4f5a;
    --icon-phone: #2a5fb8;
    --icon-mail: #5aa23a;
    --icon-pin: #d63a8c;
    --icon-social: #e0b21c;
  }
  * { margin: 0; padding: 0; box-sizing: border-box; }
  html, body { width: 1200px; height: 1200px; overflow: hidden; }
  body {
    background: var(--bg);
    font-family: "Ubuntu", sans-serif;
    position: relative;
  }
  .business-card {
    position: absolute;
    left: 100px; top: 452px;
    width: 1000px; height: 296px;
    background: var(--card);
    border-radius: 26px;
    box-shadow: 0 6px 18px rgba(0,0,0,0.12);
    overflow: hidden;
  }
  .brand {
    position: absolute;
    left: 44px; top: 150px;
    display: flex; align-items: center; gap: 14px;
  }
  .brand-dot {
    width: 30px; height: 30px; border-radius: 50%;
    background: var(--brand-blue);
  }
  .brand-name {
    font-size: 44px; font-weight: 500;
    color: var(--brand-blue);
    letter-spacing: -0.5px;
  }
  .divider-curve {
    position: absolute;
    left: 430px; top: 0;
    width: 120px; height: 296px;
  }
  .contact {
    position: absolute;
    left: 530px; top: 28px;
    color: var(--text-dark);
  }
  .person-name {
    margin-left: 55px;
    font-size: 30px; font-weight: 400;
    color: var(--name-green);
    line-height: 1;
  }
  .person-role {
    margin-left: 55px;
    margin-top: 6px;
    font-size: 19px;
    color: var(--text-grey);
  }
  .contact-list { list-style: none; margin-top: 16px; }
  .contact-item {
    display: flex; align-items: flex-start; gap: 20px;
    font-size: 23px; font-weight: 500;
    line-height: 30px;
    margin-bottom: 14px;
  }
  .contact-item svg { flex: 0 0 34px; width: 34px; height: 30px; }
</style>
</head>
<body>
  <section class="business-card">
    <div class="brand">
      <span class="brand-dot"></span>
      <span class="brand-name">TalentaPro</span>
    </div>

    <svg class="divider-curve" viewBox="0 0 120 296" aria-hidden="true">
      <path d="M80 0 C 20 70, 20 220, 80 296 L 66 296 C 8 220, 8 70, 66 0 Z" fill="var(--curve-blue)"/>
    </svg>

    <div class="contact">
      <p class="person-name">NOME COMPLETO</p>
      <p class="person-role">Cargo ou Função</p>
      <ul class="contact-list">
        <li class="contact-item">
          <svg viewBox="0 0 34 30" aria-hidden="true"><path d="M9 4 l5 0 l2 6 l-3 3 c2 4 4 6 8 8 l3 -3 l6 2 l0 5 c-14 1 -23 -8 -21 -21 z" fill="var(--icon-phone)"/></svg>
          <span>00 0000-0000 | 00 0000-0000</span>
        </li>
        <li class="contact-item">
          <svg viewBox="0 0 34 30" aria-hidden="true"><rect x="3" y="6" width="28" height="19" fill="none" stroke="var(--icon-mail)" stroke-width="2.5"/><path d="M3 6 L17 17 L31 6" fill="none" stroke="var(--icon-mail)" stroke-width="2.5"/></svg>
          <span>seuemail@talentapro.com</span>
        </li>
        <li class="contact-item">
          <svg viewBox="0 0 34 30" aria-hidden="true"><path d="M17 29 C 8 18, 7 14, 7 11 a10 10 0 0 1 20 0 c0 3 -1 7 -10 18 z" fill="var(--icon-pin)"/><circle cx="17" cy="11" r="4" fill="#fff"/></svg>
          <span>Rua nome da rua, 00, bairro<br>Cidade - Estado e CEP</span>
        </li>
        <li class="contact-item">
          <svg viewBox="0 0 34 30" aria-hidden="true"><circle cx="17" cy="15" r="10" fill="var(--icon-social)"/></svg>
          <span>@talentapro</span>
        </li>
      </ul>
    </div>
  </section>
</body>
</html>
```